Card for modern wood artisan that builds log homes and timber frames.

Design a card with catchy imagery. With a quick list of things I build and services I offer.

I'd like an English side and a french side. I can provide the text.

I am basically a guy that builds log homes and timber frames , but I am very eco friendly oriented.

I use only eco friendly products to limit my carbon footprint.
I want the client to feel as if they are hiring a good smart builder.

I have been building for a while but just starting out to market myself out there , not just work for other companies. Starting
My own thing legitimately.

I am very conscientious, and I take care of the work I do. I am trying to bring a new age, modern feel to an old profession.

Reason: I am not completely satisfied with A model yet, looking for that masculin rustic artistic design that I havent completely found yet. Thank you for your sumbissions.

Target Market(s)

People looking to hire a builder to design and build their projects.
And contractors that want to hire a quality subcontractor for their jobs.

Industry/Entity Type

Construction

Contact Information for Business Card

I want my logo on it, that I had designed here.
And a list of services I provide.

With my phone number, website adress and Email.

Requirements
Must have
• Artful presentation,
• Eco friendly feel
• I love trees.

```html
<!DOCTYPE html>
<html lang="en">
<head>
<meta charset="utf-8">
<title>Haldwood business cards</title>
<link rel="stylesheet" href="https://fonts.googleapis.com/css2?family=Open+Sans:wght@400;600;700&display=swap">
<style>
  :root {
    --backdrop: #e6e3de;
    --card: #efefee;
    --ink: #1c1c1c;
    --gold: #d9930f;
    --gold-light: #e9b54a;
    --band-black: #0d0d0d;
    --on-gold: #1c1c1c;
    --on-black: #e9b54a;
  }
  * { box-sizing: border-box; margin: 0; padding: 0; }
  html, body {
    width: 1200px; height: 900px; overflow: hidden;
    background: var(--backdrop);
    font-family: "Open Sans", Arial, sans-serif;
  }
  .sheet {
    width: 1200px; height: 900px;
    display: flex; flex-direction: column;
    align-items: center; justify-content: center; gap: 36px;
  }
  .card {
    position: relative;
    width: 700px; height: 400px;
    background: var(--card);
    box-shadow: 0 6px 18px rgba(0,0,0,.18);
    overflow: hidden;
  }
  .brand {
    position: absolute; left: 60px; top: 52px;
    display: flex; align-items: center; gap: 12px;
    color: var(--ink);
    font-weight: 700; font-size: 34px; letter-spacing: 2px;
  }
  .brand-square { width: 34px; height: 34px; background: var(--ink); }
  .person { position: absolute; left: 60px; top: 160px; }
  .person-name {
    color: var(--gold); font-weight: 600; font-size: 24px;
    letter-spacing: .5px; line-height: 1.1;
  }
  .person-role { color: var(--ink); font-size: 18px; line-height: 1.3; }
  .contacts {
    position: absolute; left: 64px; top: 238px;
    list-style: none; color: var(--ink); font-size: 18px;
  }
  .contacts li { display: flex; align-items: center; gap: 12px; height: 30px; }
  .contacts svg { width: 16px; height: 16px; fill: var(--gold); flex: none; }
  .tree-art {
    position: absolute; right: 70px; top: 40px;
    width: 130px; height: 260px;
    background: linear-gradient(180deg, var(--gold-light), var(--gold));
  }
  .band {
    position: absolute; left: 0; right: 0; bottom: 0; height: 44px;
    display: flex; align-items: center; padding: 0 60px;
  }
  .band--gold { background: var(--gold); color: var(--on-gold); }
  .band--black { background: var(--band-black); color: var(--on-black); }
  .services {
    list-style: none; display: flex; gap: 10px;
    font-size: 15px; font-weight: 600; letter-spacing: .3px; white-space: nowrap;
  }
  .services li + li::before { content: "·"; margin-right: 10px; }
</style>
</head>
<body>
<main class="sheet">

  <article class="card card--fr" lang="fr">
    <div class="brand"><span class="brand-square"></span>HALDWOOD</div>
    <div class="person">
      <p class="person-name">MATHIS LECLAIR</p>
      <p class="person-role">Directeur général</p>
    </div>
    <ul class="contacts">
      <li><svg viewBox="0 0 16 16"><path d="M3.5 1.5l2.5 0 1 3.5-1.7 1.2a9 9 0 0 0 4.5 4.5L11 9l3.5 1v2.5c0 1-1 2-2 2A11 11 0 0 1 1.5 3.5c0-1 1-2 2-2z"/></svg>555 0142 777</li>
      <li><svg viewBox="0 0 16 16"><path d="M1 3h14v10H1z M1.6 3.6L8 8.5l6.4-4.9" fill="var(--gold)" stroke="#fff" stroke-width="1.2"/></svg>hello@haldwood.com</li>
      <li><svg viewBox="0 0 16 16"><circle cx="8" cy="8" r="7"/></svg>www.haldwood.com</li>
    </ul>
    <div class="tree-art" role="img" aria-label="Golden pine tree illustration with roots, carrying the company name"></div>
    <div class="band band--gold">
      <ul class="services">
        <li>Maisons en rondins</li>
        <li>Charpentes de bois</li>
        <li>Construction écologique</li>
      </ul>
    </div>
  </article>

  <article class="card card--en">
    <div class="brand"><span class="brand-square"></span>HALDWOOD</div>
    <div class="person">
      <p class="person-name">MATHIS LECLAIR</p>
      <p class="person-role">Managing Director</p>
    </div>
    <ul class="contacts">
      <li><svg viewBox="0 0 16 16"><path d="M3.5 1.5l2.5 0 1 3.5-1.7 1.2a9 9 0 0 0 4.5 4.5L11 9l3.5 1v2.5c0 1-1 2-2 2A11 11 0 0 1 1.5 3.5c0-1 1-2 2-2z"/></svg>555 0142 777</li>
      <li><svg viewBox="0 0 16 16"><path d="M1 3h14v10H1z M1.6 3.6L8 8.5l6.4-4.9" fill="var(--gold)" stroke="#fff" stroke-width="1.2"/></svg>hello@haldwood.com</li>
      <li><svg viewBox="0 0 16 16"><circle cx="8" cy="8" r="7"/></svg>www.haldwood.com</li>
    </ul>
    <div class="tree-art" role="img" aria-label="Golden pine tree illustration with roots, carrying the company name"></div>
    <div class="band band--black">
      <ul class="services">
        <li>Log homes</li>
        <li>Timber frames</li>
        <li>Eco-friendly builds</li>
        <li>Subcontracting</li>
      </ul>
    </div>
  </article>

</main>
</body>
</html>
```